Web Design Project for a new download application :-)

We need a website design and a logo design for a new website and desktop application.
The Website will be www.Fetchora.com
The installed application will be: Fetchora

Fetchora is a desktop application that searches and finds all kind of Media files (Movies, Games, Songs, software, etc..)
Fetchora will also manage the download process for the selected files.
Fetchora automates the whole search and download process.

User Flow:
users will initially visit the website.
user will download the application from the website
user will install the application on his computer.
user will run and use the application.

What makes our software special:
-Great search engine for searching media files.
-Very high speed downloads. maximum speeds.
-Allow used to Search by: file type, size, date, format
-Pause and resume downloads
-Get any file you want instantly.
-Unlimited Downloads.

We will need:
Logo
WebSite Design
Icons for the desktop application.

we need only PSDs - no codded pages are needed !

Design to the following screen Size & resolution: 1024 x 768

Target Market(s)

movies and music lovers.
users who download movies, games, softwares, music etc...

Industry/Entity Type

Software

Requirements
Must have
• must have download button

```html
<!DOCTYPE html>
<html lang="en">
<head>
<meta charset="utf-8">
<title>Fetchora – Find and download media fast</title>
<link rel="stylesheet" href="https://fonts.googleapis.com/css2?family=Arimo:wght@400;700&display=swap">
<style>
  :root {
    --brand-blue: #2a6db5;
    --brand-dark: #1b4f8a;
    --hero-top: #1d5ea8;
    --hero-bottom: #0f3f7c;
    --text-dark: #222;
    --text-muted: #555;
    --line: #d8d8d8;
    --panel: #f2f2f4;
    --footer-bg: #333;
    --footer-text: #b9b9b9;
    --white: #fff;
  }
  * { box-sizing: border-box; margin: 0; padding: 0; }
  html, body { width: 1200px; height: 929px; overflow: hidden; }
  body {
    font-family: "Arimo", Arial, sans-serif;
    background: linear-gradient(#fff, #f7f7f7);
    color: var(--text-dark);
    position: relative;
  }
  .site-header { position: absolute; top: 0; left: 0; width: 1200px; height: 109px; background: var(--white); }
  .brand {
    position: absolute; left: 68px; top: 36px;
    display: flex; align-items: center; gap: 10px;
    font-size: 46px; font-weight: 700; color: var(--brand-blue); letter-spacing: -1px;
  }
  .brand-dot { width: 18px; height: 18px; border-radius: 50%; background: var(--brand-blue); }
  .main-nav { position: absolute; top: 40px; left: 686px; display: flex; align-items: center; font-size: 17px; font-weight: 700; color: #444; }
  .main-nav a { color: inherit; text-decoration: none; }
  .main-nav .sep { margin: 0 10px; color: #666; font-weight: 400; }
  .nav-current {
    display: inline-block; width: 82px; height: 28px; line-height: 28px; text-align: center;
    color: var(--white) !important; border-radius: 14px; margin-right: 16px;
    background: linear-gradient(#4a8ad6, #1b5aa8); box-shadow: inset 0 1px 0 rgba(255,255,255,.4), 0 0 0 1px #174a8a;
  }
  .hero {
    position: absolute; top: 109px; left: 0; width: 1200px; height: 401px;
    background: radial-gradient(ellipse at 55% 30%, #3f82c9 0%, var(--hero-top) 40%, var(--hero-bottom) 100%);
  }
  .hero-title { position: absolute; left: 68px; top: 52px; color: var(--white); font-size: 46px; line-height: 46px; font-weight: 700; text-shadow: 0 2px 4px rgba(0,0,0,.3); }
  .hero-text { position: absolute; left: 68px; top: 172px; width: 490px; color: var(--white); font-size: 18.5px; line-height: 22px; }
  .btn { position: absolute; top: 295px; height: 42px; border-radius: 4px; font-size: 19px; font-weight: 700; display: flex; align-items: center; justify-content: center; }
  .btn-download { left: 66px; width: 218px; background: linear-gradient(#f4f4f4, #bdbdbd); color: #111; padding-left: 48px; box-shadow: 0 2px 4px rgba(0,0,0,.3); }
  .btn-download .btn-icon { position: absolute; left: -2px; top: -4px; width: 52px; height: 52px; border-radius: 50%; background: radial-gradient(#555, #111); border: 2px solid #ddd; }
  .btn-read { left: 296px; width: 158px; background: linear-gradient(#7cc0f5, #3a8be0); color: var(--white); box-shadow: 0 2px 4px rgba(0,0,0,.3); border: 1px solid #9fd0fa; }
  .hero-visual {
    position: absolute; left: 606px; top: 24px; width: 520px; height: 377px;
    border-radius: 12px 12px 0 0;
    background: linear-gradient(160deg, #2b2b2b 0%, #111 60%, #3a3a3a 100%);
    box-shadow: inset 0 0 0 16px #1a1a1a;
  }
  .hero-visual::after { content: ""; position: absolute; left: 22px; top: 22px; right: 22px; bottom: 40px; background: linear-gradient(#dde9f7, #b8cfe9); }
  .features-title { position: absolute; left: 72px; top: 537px; font-size: 22px; font-weight: 700; color: var(--brand-dark); }
  .rule { position: absolute; left: 68px; top: 575px; width: 1056px; height: 1px; background: var(--line); }
  .feature { position: absolute; top: 605px; width: 340px; }
  .feature-icon {
    position: absolute; left: 0; top: 0; width: 98px; height: 87px; border-radius: 4px;
    background: linear-gradient(#fff, #f0f0f0); border: 1px solid #d6d6d6; box-shadow: 0 1px 3px rgba(0,0,0,.1);
    display: flex; align-items: center; justify-content: center;
  }
  .feature-copy { position: absolute; left: 112px; top: 0; width: 240px; font-size: 16.5px; line-height: 23px; }
  .feature-copy strong { display: block; }
  .testimonial { position: absolute; left: 68px; top: 730px; width: 1056px; height: 69px; background: var(--white); border: 1px solid #e4e4e4; }
  .testimonial-label {
    position: absolute; left: 0; top: 0; width: 230px; height: 67px; background: var(--panel);
    clip-path: polygon(0 0, 90% 0, 100% 50%, 90% 100%, 0 100%);
    font-size: 22px; color: var(--brand-dark); display: flex; align-items: center; padding-left: 30px;
  }
  .testimonial-quote { position: absolute; left: 260px; top: 15px; width: 780px; font-size: 14.5px; line-height: 20px; color: var(--text-dark); }
  .site-footer { position: absolute; left: 0; top: 836px; width: 1200px; height: 93px; background: var(--footer-bg); color: var(--footer-text); font-size: 14.5px; }
  .copyright { position: absolute; left: 68px; top: 19px; }
  .footer-links { position: absolute; left: 68px; top: 39px; }
  .footer-links span { margin: 0 8px; }
  .social { position: absolute; top: 16px; width: 36px; height: 36px; border-radius: 4px; }
  .social-one { left: 1039px; background: #3b5a9a; }
  .social-two { left: 1082px; background: #5fc4ea; }
</style>
</head>
<body>
  <header class="site-header">
    <div class="brand"><span class="brand-dot"></span>Fetchora</div>
    <nav class="main-nav">
      <a class="nav-current" href="#">Home</a>
      <a href="#">About</a><span class="sep">|</span>
      <a href="#">Download</a><span class="sep">|</span>
      <a href="#">Blog</a><span class="sep">|</span>
      <a href="#">Contact</a>
    </nav>
  </header>

  <section class="hero">
    <h1 class="hero-title">your website<br>caption goes here</h1>
    <p class="hero-text">Lorem ipsum dolor sit amet, consectetur adipiscing elit. Morbi vestibulum augue turpis. Suspendisse porttitor dui nec risus malesuada eget porttitor enim elementum. Quisque nec tincidunt massa.</p>
    <a class="btn btn-download"><span class="btn-icon"></span>Download Now</a>
    <a class="btn btn-read">Read More</a>
    <div class="hero-visual" role="img" aria-label="Desktop monitor showing the Fetchora search application with a magnified search panel"></div>
  </section>

  <h2 class="features-title">Features &amp; Benefits</h2>
  <div class="rule"></div>

  <div class="feature" style="left:68px">
    <div class="feature-icon">
      <svg width="56" height="40" viewBox="0 0 56 40" aria-hidden="true">
        <path d="M4 24 L18 10 L30 14 L40 8 L52 20 L34 34 Z" fill="#2a6db5"/>
        <rect x="0" y="26" width="10" height="6" fill="#1b4f8a" transform="rotate(-45 5 29)"/>
      </svg>
    </div>
    <div class="feature-copy"><strong>Pharetra faucibus luctus.</strong>Nulla facilisi. Donec eget mau vitae orci dignissim accumsan. Donec vulputate lorem vitae.</div>
  </div>

  <div class="feature" style="left:428px">
    <div class="feature-icon">
      <svg width="56" height="48" viewBox="0 0 56 48" aria-hidden="true">
        <circle cx="22" cy="30" r="14" fill="none" stroke="#2a6db5" stroke-width="8" stroke-dasharray="5 3"/>
        <circle cx="22" cy="30" r="4" fill="#2a6db5"/>
        <circle cx="42" cy="12" r="7" fill="none" stroke="#555" stroke-width="5" stroke-dasharray="3 2"/>
      </svg>
    </div>
    <div class="feature-copy"><strong>Pharetra faucibus luctus.</strong>Nulla facilisi. Donec eget mau vitae orci dignissim accumsan. Donec vulputate lorem vitae.</div>
  </div>

  <div class="feature" style="left:791px">
    <div class="feature-icon">
      <svg width="60" height="48" viewBox="0 0 60 48" aria-hidden="true">
        <rect x="4" y="18" width="40" height="26" fill="#666"/>
        <path d="M4 18 L24 34 L44 18" fill="none" stroke="#fff" stroke-width="2"/>
        <circle cx="38" cy="14" r="10" fill="none" stroke="#2a6db5" stroke-width="5"/>
        <line x1="45" y1="21" x2="54" y2="30" stroke="#2a6db5" stroke-width="6" stroke-linecap="round"/>
      </svg>
    </div>
    <div class="feature-copy"><strong>Pharetra faucibus luctus.</strong>Nulla facilisi. Donec eget mau vitae orci dignissim accumsan. Donec vulputate lorem vitae.</div>
  </div>

  <section class="testimonial">
    <div class="testimonial-label">Happy Users say</div>
    <p class="testimonial-quote">“Lorem ipsum dolor sit amet, consectetur adipiscing elit. Sed vel dui purus. Ut tincidunt convallis gravida. Duis consequat, lorem, massa enim iaculis lectus, quis cursus du dui a sapien. Sed pulvinar tempus enim.” <strong>Martin, Perth</strong></p>
  </section>

  <footer class="site-footer">
    <p class="copyright">Copyright © 2011 Fetchora. All rights Reserved.</p>
    <p class="footer-links">Terms<span>|</span>About Us<span>|</span>Contact Us</p>
    <span class="social social-one"></span>
    <span class="social social-two"></span>
  </footer>
</body>
</html>
```